依頼詳細
国家資格に対応するための新規講習の開講を予定しまして新しいチラシを作成したいと思っております。
令和5年5月リリース予定の新規講習に関しましての広告及び講習に関する説明を行えるチラシのデザインをお願いいたします。
令和5年5月リリース予定ですが、既存の講習受講後に新規講習を追加で受ける形の受講も可能であるため、それまでの間の従来の講習も広告も行っていきたいと思っております。
従来の講習→新規講習の受講の流れを勧めたいです。

利用用途は新聞折込及び、ポスティングにて利用いたします。
希望はA4片面カラーを希望いたします。

納品はpsdファイルおよびPDFファイル(プリモアにすぐに入稿できる仕様)を希望いたします。
記載項目
■校名
ドローン教習所 翠光小樽校・道央MTR校
■空撮技能認定ロゴ

```html
<!DOCTYPE html>
<html lang="ja">
<head>
<meta charset="UTF-8">
<title>ドローン教習所 翠光小樽校・道央MTR校</title>
<link href="https://fonts.googleapis.com/css2?family=Noto+Sans+JP:wght@400;500;700;900&display=swap" rel="stylesheet">
<style>
:root{
  --sky-top:#2f8fe0;
  --sky-bottom:#cfe9fb;
  --navy:#0d3f8f;
  --blue:#1f6fd1;
  --light-blue:#e6f3fd;
  --gold:#c99a2e;
  --gold-light:#f3d57a;
  --red:#d8262c;
  --orange:#f08c00;
  --ink:#1d2433;
  --white:#ffffff;
  --grass:#6c9b3e;
}
*{margin:0;padding:0;box-sizing:border-box}
html,body{width:844px;height:1200px;overflow:hidden;background:#fff}
body{font-family:"Noto Sans JP",sans-serif;color:var(--ink)}
.flyer{position:relative;width:844px;height:1200px;overflow:hidden;background:var(--white)}
.hero{position:absolute;left:0;top:0;width:844px;height:660px;background:linear-gradient(180deg,var(--sky-top) 0%,#7cc0f1 45%,var(--sky-bottom) 100%)}
.cert-line{position:absolute;left:0;top:14px;width:844px;text-align:center;color:var(--white);font-weight:700;font-size:26px;letter-spacing:4px}
.brand{position:absolute;right:24px;top:14px;display:flex;align-items:center;gap:8px;background:var(--white);padding:6px 12px;border-radius:6px}
.brand-dot{width:18px;height:18px;border-radius:50%;background:var(--blue)}
.brand-name{font-weight:900;font-size:18px;color:var(--navy)}
.title{position:absolute;left:0;top:50px;width:844px;text-align:center;font-weight:900;font-size:104px;line-height:1;color:var(--white);-webkit-text-stroke:8px var(--navy);paint-order:stroke fill;letter-spacing:4px}
.school{position:absolute;left:50%;top:168px;transform:translateX(-50%);background:var(--white);color:var(--navy);font-weight:900;font-size:24px;padding:4px 22px;border-radius:4px;white-space:nowrap}
.drone-photo{position:absolute;left:330px;top:160px;width:500px;height:250px;border-radius:6px;background:radial-gradient(ellipse at 55% 55%,#9aa3ad 0%,#c9d7e4 35%,rgba(207,233,251,0) 70%)}
.badge{position:absolute;left:28px;top:210px;width:300px;height:200px}
.level-badge{position:absolute;left:340px;top:320px;width:70px;height:70px;border-radius:50%;background:var(--blue);border:4px solid var(--white)}
.wants{position:absolute;left:20px;top:424px;width:804px;display:flex;gap:12px}
.want{flex:1;display:flex;align-items:center;gap:10px;background:var(--white);border:3px solid var(--blue);border-radius:6px;padding:8px 10px;font-weight:700;font-size:16px;line-height:1.35;color:var(--navy)}
.want svg{flex:none}
.uses{position:absolute;left:20px;top:500px;width:804px;display:flex;gap:6px}
.use{position:relative;flex:1;height:140px;border-radius:4px}
.use-label{position:absolute;left:0;top:0;width:100%;text-align:center;font-weight:900;font-size:24px;color:var(--white);-webkit-text-stroke:4px var(--navy);paint-order:stroke fill;padding-top:4px}
.use.aerial{background:linear-gradient(180deg,#8fc4ec,#4f7f4a)}
.use.inspect{background:linear-gradient(180deg,#a9bccb,#6d7b86)}
.use.survey{background:linear-gradient(180deg,#b8d7a6,#6e8a4f)}
.use.spray{background:linear-gradient(180deg,#b7d99a,var(--grass))}
.scenes{position:absolute;left:20px;top:646px;width:804px;background:var(--white);color:var(--navy);font-weight:700;font-size:18px;text-align:center;padding:4px 0;border-radius:3px}
.basic{position:absolute;left:20px;top:688px;width:804px;height:180px;display:flex;gap:14px}
.basic-price{width:230px;flex:none}
.tag{display:inline-block;background:var(--blue);color:var(--white);font-weight:900;font-size:20px;padding:4px 12px;border-radius:3px}
.price-line{display:flex;align-items:center;gap:6px;margin-top:8px;white-space:nowrap}
.price-label{flex:none;background:var(--navy);color:var(--white);font-size:12px;font-weight:700;border-radius:50%;width:46px;height:46px;display:flex;align-items:center;justify-content:center;text-align:center;line-height:1.1}
.price{font-weight:900;font-size:42px;color:var(--red);line-height:1;white-space:nowrap}
.price small{font-size:18px}
.price-note{font-size:12px;line-height:1.6;margin-top:6px;color:var(--ink)}
.basic-notes{flex:1;font-size:11.5px;line-height:1.75;padding-top:4px}
.basic-info{width:250px;flex:none;font-size:12px;line-height:1.7}
.info-head{font-weight:900;color:var(--navy);font-size:13px}
.exam-band{position:absolute;left:0;top:874px;width:844px;height:48px;background:var(--orange);display:flex;align-items:center;padding-left:24px;gap:24px}
.exam-band h2{font-weight:900;font-size:32px;color:var(--white);white-space:nowrap}
.exam-band p{font-size:11px;color:var(--white);line-height:1.45;font-weight:500}
.exam{position:absolute;left:20px;top:932px;width:804px;height:150px;display:flex;gap:14px}
.exam-price{width:230px;flex:none}
.exam .price{font-size:40px}
.exam .tag{background:var(--orange)}
.exam-notes{flex:1;font-size:12px;line-height:1.7}
.exam-notes strong{color:var(--red)}
.exam-figure{width:150px;height:150px;flex:none;border-radius:6px;background:linear-gradient(180deg,#fde6c4,#f5c27a)}
.footer{position:absolute;left:0;top:1090px;width:844px;height:110px;background:var(--light-blue);border-top:4px solid var(--blue);display:flex;padding:12px 20px;gap:20px}
.footer-school{width:360px;flex:none}
.footer-school h3{font-weight:900;font-size:24px;color:var(--navy)}
.footer-school ul{list-style:none;font-size:11px;line-height:1.55;margin-top:4px;display:grid;grid-template-columns:1fr 1fr;column-gap:10px}
.footer-contact{flex:1}
.footer-contact .lead{display:inline-block;background:var(--navy);color:var(--white);font-size:14px;font-weight:700;padding:2px 10px;border-radius:3px}
.phone{display:flex;align-items:center;gap:8px;font-weight:900;font-size:40px;color:var(--navy);line-height:1.1;margin-top:2px;white-space:nowrap}
.web{font-size:12px;line-height:1.4}
</style>
</head>
<body>
<main class="flyer">
  <section class="hero">
    <p class="cert-line">空撮技能認定協会認定</p>
    <div class="brand"><span class="brand-dot"></span><span class="brand-name">空撮技能認定</span></div>
    <h1 class="title">ドローン教習所</h1>
    <p class="school">翠光小樽校・道央MTR校</p>
    <div class="drone-photo" role="img" aria-label="空に浮かぶドローンと操縦する人の写真"></div>
    <svg class="badge" viewBox="0 0 300 200" aria-label="2日間で取得できます 操縦技能証明書 国土交通省認定">
      <circle cx="120" cy="88" r="86" fill="#c99a2e"/>
      <circle cx="120" cy="88" r="76" fill="#f3d57a" stroke="#fff" stroke-width="3"/>
      <text x="120" y="90" text-anchor="middle" font-family="Noto Sans JP, sans-serif" font-weight="900" font-size="42" fill="#b51f24">2日間で</text>
      <text x="120" y="124" text-anchor="middle" font-family="Noto Sans JP, sans-serif" font-weight="900" font-size="24" fill="#0d3f8f">取得できます</text>
      <rect x="10" y="138" width="220" height="38" fill="#d8262c"/>
      <text x="120" y="165" text-anchor="middle" font-family="Noto Sans JP, sans-serif" font-weight="900" font-size="24" fill="#fff">操縦技能証明書</text>
      <text x="120" y="195" text-anchor="middle" font-family="Noto Sans JP, sans-serif" font-weight="700" font-size="14" fill="#0d3f8f">国土交通省認定</text>
    </svg>
    <div class="level-badge" aria-label="講習レベルの認定バッジ"></div>

    <div class="wants">
      <div class="want">ドローンで空からの<br>景色を撮りたい方
        <svg width="34" height="34" viewBox="0 0 34 34"><rect x="2" y="2" width="30" height="30" fill="#fff" stroke="#0d3f8f" stroke-width="3"/><path d="M8 17l7 7 13-16" fill="none" stroke="#0d3f8f" stroke-width="4"/></svg></div>
      <div class="want">ドローンレースに<br>出場したい!
        <svg width="34" height="34" viewBox="0 0 34 34"><rect x="2" y="2" width="30" height="30" fill="#fff" stroke="#0d3f8f" stroke-width="3"/><path d="M8 17l7 7 13-16" fill="none" stroke="#0d3f8f" stroke-width="4"/></svg></div>
      <div class="want">ドローンを使って農薬の<br>空中散布をしたい方
        <svg width="34" height="34" viewBox="0 0 34 34"><rect x="2" y="2" width="30" height="30" fill="#fff" stroke="#0d3f8f" stroke-width="3"/><path d="M8 17l7 7 13-16" fill="none" stroke="#0d3f8f" stroke-width="4"/></svg></div>
    </div>

    <div class="uses">
      <div class="use aerial" role="img" aria-label="空撮の写真"><span class="use-label">空撮</span></div>
      <div class="use inspect" role="img" aria-label="点検の写真"><span class="use-label">点検</span></div>
      <div class="use survey" role="img" aria-label="測量の写真"><span class="use-label">測量</span></div>
      <div class="use spray" role="img" aria-label="農薬散布の写真"><span class="use-label">農薬散布</span></div>
    </div>
    <p class="scenes">・空撮・点検・レース・広告・測量・農薬散布など様々なシーンで活用いただけます</p>
  </section>

  <section class="basic">
    <div class="basic-price">
      <span class="tag">基礎技能講習</span>
      <div class="price-line"><span class="price-label">受講料</span><span class="price">99,000<small>円</small></span></div>
      <p class="price-note">(1日目 22,000円税込)<br>(2日目 77,000円税込)</p>
    </div>
    <div class="basic-notes">
      内容<br>
      ・ドローンの基礎知識と安全な飛行ルールを学びます<br>
      ・座学と実技を組み合わせた二日間の講習です<br>
      ・修了時に操縦技能証明書を発行いたします<br>
      ・機体は教習所で用意しますので手ぶらで受講可能<br>
      ・修了後は国家試験講習へ続けて受講できます<br>
      ・少人数制で初心者の方も安心して学べます
    </div>
    <div class="basic-info">
      <p class="info-head">取得可能ライセンス</p>
      1日目 入門認定資格・初級(基本)<br>
      2日目 上級認定資格・中級(応用)<br>
      <p class="info-head">講習日程　9時～18時</p>
      1日目 座学・基礎飛行<br>
      2日目 実技・応用飛行・修了試験
    </div>
  </section>

  <div class="exam-band">
    <h2>国家試験コース開講!</h2>
    <p>令和5年5月より国家資格に対応した新しい講習を開講します。<br>基礎技能講習を修了された方は追加受講でスムーズに国家資格を目指せます。</p>
  </div>

  <section class="exam">
    <div class="exam-price">
      <span class="tag">国家試験講習</span>
      <div class="price-line"><span class="price-label">受講料</span><span class="price">112,200<small>円</small></span></div>
      <p class="price-note">(基礎技能講習修了者は割引あり)</p>
    </div>
    <div class="exam-notes">
      学科講習・実地講習があり、実地講習では<strong>ドローン</strong>を使って飛行技能を身につけます。<br>
      ドローン教習所で基礎技能講習を受講した方は、学科の一部が免除となります。<br>
      ・1日目 学科講習　・2日目 実地講習<br>
      ・3日目 修了審査　※日程は変更になる場合があります
    </div>
    <div class="exam-figure" role="img" aria-label="ドローンを操縦する受講者のイラスト"></div>
  </section>

  <footer class="footer">
    <div class="footer-school">
      <h3>ドローン教習所 翠光小樽校</h3>
      <ul>
        <li>・みなと小樽自動車学校</li>
        <li>・北星自動車学校</li>
        <li>・道央MTR校</li>
        <li>・南嶺自動車学校</li>
      </ul>
    </div>
    <div class="footer-contact">
      <span class="lead">詳細は弊社webサイトでご確認ください</span>
      <div class="phone">
        <svg width="36" height="36" viewBox="0 0 24 24" aria-hidden="true"><path fill="#0d3f8f" d="M6.6 10.8a15.1 15.1 0 0 0 6.6 6.6l2.2-2.2a1 1 0 0 1 1-.25 11.4 11.4 0 0 0 3.6.57 1 1 0 0 1 1 1V20a1 1 0 0 1-1 1A17 17 0 0 1 3 4a1 1 0 0 1 1-1h3.5a1 1 0 0 1 1 1c0 1.25.2 2.45.57 3.57a1 1 0 0 1-.25 1z"/></svg>
        0134-00-2468
      </div>
      <p class="web">info-drone@suiko-g.example　www.suiko-g.example/drone/</p>
    </div>
  </footer>
</main>
</body>
</html>
```